A label for a gin called Rhubarb Sherbet Twist Gin

We have attached a mood board below of images that reflect how we would like the label to feel. The words "Rhubarb Sherbet Twist Gin" are the only important bits that need to be clearly visible.

Font styles to use
Decorative

Colors
eda3c7
e667a6
b768aa
d2a4cc

```html
<!DOCTYPE html>
<html lang="en">
<head>
<meta charset="utf-8">
<title>Rhubarb Sherbet Twist Gin – Label</title>
<link rel="stylesheet" href="https://fonts.googleapis.com/css2?family=Kalam:wght@400&display=swap">
<style>
  :root {
    --canvas-bg: #f4f4f4;
    --label-pink: #eda3c7;
    --label-glow: #ffffff;
    --hot-pink: #e667a6;
    --plum: #b768aa;
    --lilac: #d2a4cc;
  }

  html, body {
    margin: 0;
    padding: 0;
    width: 1200px;
    height: 2625px;
    overflow: hidden;
    background: var(--canvas-bg);
  }

  .canvas {
    position: relative;
    width: 1200px;
    height: 2625px;
    display: flex;
    align-items: center;
    justify-content: center;
  }

  .gin-label {
    position: relative;
    width: 1000px;
    height: 1310px;
    background:
      radial-gradient(ellipse 55% 42% at 50% 52%, var(--label-glow) 0%, rgba(255,255,255,0.55) 35%, rgba(255,255,255,0) 75%),
      var(--label-pink);
    display: flex;
    flex-direction: column;
    align-items: center;
    box-sizing: border-box;
    padding-top: 70px;
  }

  .brand-emblem {
    width: 400px;
    height: 380px;
    border-radius: 40px 40px 8px 8px;
    background: linear-gradient(180deg, var(--lilac) 0%, var(--hot-pink) 100%);
    opacity: 0.85;
  }

  .product-name {
    margin: 150px 0 0;
    font-family: "Kalam", cursive;
    font-weight: 400;
    color: var(--plum);
    text-align: center;
    line-height: 1.05;
  }

  .product-name__top {
    display: block;
    font-size: 118px;
    letter-spacing: -1px;
  }

  .product-name__bottom {
    display: block;
    font-size: 128px;
    margin-top: 10px;
  }

  .product-name__spirit {
    font-size: 190px;
  }
</style>
</head>
<body>
  <main class="canvas">
    <section class="gin-label">
      <div class="brand-emblem" role="img" aria-label="Pink striped circus tent emblem"></div>
      <h1 class="product-name">
        <span class="product-name__top">Rhubarb Sherbet</span>
        <span class="product-name__bottom">Twist <span class="product-name__spirit">Gin</span></span>
      </h1>
    </section>
  </main>
</body>
</html>
```